LinkedIn Engagement Posts for Bookkeeping Company

The task is to complete 20 engaging posts for our LinkedIn page. These posts should ask a question, take a poll, provide useful information or interesting articles. These should NOT be advertisements for our services. Our target audience is business owners (small and mid-size businesses). The content should be relevant to business owners/entrepreneurs. Topics should include content about making money, accounting/bookkeeping info, operating a business, cashflow, etc.

We use LedgerNest Cloud for our services, so do not refer to any other accounting software (unless it is a comparison showing advantages of LNC).

Our website:
https://www.brightquillbooks.example/

Target Market(s)

Business owners/entrepreneurs (Small & Mid-Sized Businesses)

Industry/Entity Type

Accounting company that provides bookkeeping services, financial reporting and payroll processing (does not provide tax services!)

Font styles to use
Serif
Sans Serif

Colors
0054AA
0677BA
7BADD7
CADEEF
E8F1F8

Requirements
Must have
• 20 Engaging posts for LinkedIn, including hashtags
Nice to have
• Stay with current branding for overall design graphics (see website and social media accounts)
Should not have
• We do not provide tax or audit services, so please do not include these topics other that to say you must have accurate and updated bookkeeping in order to complete taxes and/or in the event of an audit.

```html
<!DOCTYPE html>
<html lang="en">
<head>
<meta charset="utf-8">
<title>Brightquill Books – Weekly Bookkeeping Hours Poll</title>
<link rel="stylesheet" href="https://fonts.googleapis.com/css2?family=Archivo:wght@400;500;800&family=Tinos&display=swap">
<style>
  :root {
    --bg: #eaf3f6;
    --card: #ffffff;
    --teal: #38b4cf;
    --navy: #1b3f6d;
    --brand-navy: #174a7c;
    --button: #0f4f80;
    --white: #ffffff;
  }
  * { margin: 0; padding: 0; box-sizing: border-box; }
  html, body { width: 1200px; height: 1200px; overflow: hidden; }
  body {
    background: var(--bg);
    position: relative;
    font-family: "Archivo", Arial, sans-serif;
    color: var(--navy);
  }
  .brand {
    position: absolute;
    top: 108px;
    left: 0;
    width: 1200px;
    text-align: center;
    font-family: "Tinos", "Times New Roman", serif;
    font-size: 56px;
    color: var(--brand-navy);
    letter-spacing: 0.5px;
  }
  .poll-card {
    position: absolute;
    left: 265px;
    top: 261px;
    width: 664px;
    height: 811px;
    background: var(--card);
    box-shadow: 0 24px 40px rgba(40, 80, 100, 0.12);
  }
  .poll-card__band {
    position: absolute;
    left: 0;
    top: 0;
    width: 664px;
    height: 248px;
  }
  .poll-card__question {
    position: absolute;
    left: 0;
    top: 38px;
    width: 664px;
    text-align: center;
    font-size: 33px;
    line-height: 48px;
    font-weight: 400;
    letter-spacing: 0.2px;
  }
  .poll-card__question strong { font-weight: 800; }
  .poll-options {
    position: absolute;
    left: 74px;
    top: 290px;
    list-style: none;
  }
  .poll-option {
    display: flex;
    align-items: center;
    height: 112px;
    font-size: 66px;
    font-weight: 400;
    letter-spacing: -0.5px;
  }
  .poll-option__radio {
    width: 24px;
    height: 24px;
    border: 1.5px solid var(--teal);
    border-radius: 50%;
    margin-right: 35px;
    flex-shrink: 0;
  }
  .comment-button {
    position: absolute;
    left: 170px;
    top: 688px;
    width: 330px;
    height: 65px;
    background: var(--button);
    color: var(--white);
    font-weight: 800;
    font-size: 28px;
    display: flex;
    align-items: center;
    justify-content: center;
    letter-spacing: 0.3px;
  }
  .decor { position: absolute; }
</style>
</head>
<body>
  <div class="brand">Brightquill Books</div>

  <svg class="decor" style="left:903px;top:224px" width="48" height="48" viewBox="0 0 48 48">
    <path d="M24 4V44M4 24H44" stroke="#38b4cf" stroke-width="4"/>
  </svg>
  <svg class="decor" style="left:980px;top:460px" width="54" height="54" viewBox="0 0 54 54">
    <circle cx="27" cy="27" r="23" fill="none" stroke="#38b4cf" stroke-width="5"/>
  </svg>
  <svg class="decor" style="left:101px;top:875px" width="44" height="44" viewBox="0 0 44 44">
    <path d="M22 2V42M2 22H42" stroke="#38b4cf" stroke-width="4"/>
  </svg>

  <section class="poll-card">
    <svg class="poll-card__band" viewBox="0 0 664 248" aria-hidden="true">
      <path d="M0 0H664V177C520 225 410 247 332 247C254 247 144 225 0 177Z" fill="#38b4cf"/>
    </svg>
    <p class="poll-card__question">How many hours do you spend<br>keeping records of your<br><strong>Business Finances</strong><br>in a week?</p>
    <ul class="poll-options">
      <li class="poll-option"><span class="poll-option__radio"></span>35hrs+</li>
      <li class="poll-option"><span class="poll-option__radio"></span>50hrs+</li>
      <li class="poll-option"><span class="poll-option__radio"></span>70hrs+</li>
    </ul>
    <div class="comment-button">COMMENT</div>
  </section>

  <svg class="decor" style="left:240px;top:1034px" width="54" height="54" viewBox="0 0 54 54">
    <circle cx="27" cy="27" r="23" fill="none" stroke="#38b4cf" stroke-width="5"/>
  </svg>
</body>
</html>
```